Business and Success Coaching Business Card

Need a business card for my coaching business. I coach small businesses, career professionals and, individuals wanting to unlock their human potential and achieve excellence. At the heart of our methodology is the Shaping Purposeful Action Routines Knowingly (SPARK) approach to formulate empowerment, create principles for success and setting achievable outcomes. I would like something that incorporates our new logo, something clean and sharp with a solid darker, but complementary background, color on the card front. The back should be white where there will be room for three questions

Target Market(s)

People looking to advance and improve themselves through a success coach

Industry/Entity Type

Life Coaching

Contact Information for Business Card

Contact information on card.
Business name on front of card
Questions on back

Font styles to use
Other font styles liked:
• Century Gothic or other Serif style fonts that look similar to Century Gothic

Colors

Designer to choose colors to be used in the design.

Requirements
Must have
• Logo on front of card
• Business name - The Steady Forge
• Contact name - Ted Harlow
• Address - Box 4619, Millbrook, NE 68901-4619
• Phone number - 303-555-0147
• Email address - harlow.ted@thesteadyforge.example
• Certifications - CPC, CLC, MTT, ANLP
• Back of card
• Three questions on the back of the card:
• If you were at your best, what would you do right now?
• What is the decision you have been avoiding?
• What's one action you could take in the next 10 minutes?
Nice to have
• I would like to see a solid color on the front of the card that compliments the logo.
• Back should be white, or could be contrasting, but need to have the three questions.

```html
<!DOCTYPE html>
<html lang="en">
<head>
<meta charset="utf-8">
<title>The Steady Forge – Business Card</title>
<link href="https://fonts.googleapis.com/css2?family=Didact+Gothic&family=Mulish:wght@800&display=swap" rel="stylesheet">
<style>
  :root {
    --canvas: #e9eaec;
    --navy: #213668;
    --navy-soft: #3a5283;
    --sky: #4a86cc;
    --sky-pale: #b9c9e3;
    --ink-grey: #6b6f76;
    --white: #ffffff;
  }
  * { box-sizing: border-box; margin: 0; padding: 0; }
  html, body {
    width: 1200px; height: 900px; overflow: hidden;
    background: var(--canvas);
    font-family: "Didact Gothic", "Century Gothic", sans-serif;
  }
  .sheet {
    width: 1200px; height: 900px;
    display: flex; flex-direction: column; align-items: center; justify-content: center; gap: 40px;
  }
  .card {
    position: relative; width: 700px; height: 400px; overflow: hidden;
    box-shadow: 0 8px 24px rgba(0,0,0,.12);
  }

  /* Question side */
  .card--questions { background: var(--navy); color: var(--white); }
  .emblem-art {
    position: absolute; left: 190px; top: 60px; width: 240px; height: 170px;
    background: radial-gradient(ellipse at 50% 85%, var(--navy-soft) 0%, rgba(58,82,131,.5) 50%, rgba(33,54,104,0) 72%);
  }
  .questions {
    position: absolute; left: 60px; bottom: 56px; list-style: none;
    font-size: 20px; line-height: 1.75; letter-spacing: .3px;
  }

  /* Contact side */
  .card--contact { background: var(--white); }
  .brand { position: absolute; right: 44px; top: 44px; text-align: right; }
  .brand__name {
    font-family: "Mulish", "Century Gothic", sans-serif; font-weight: 800;
    font-size: 27px; color: var(--navy);
  }
  .brand__tagline { font-size: 13px; color: var(--sky-pale); margin-top: 2px; }
  .summit-band { position: absolute; left: 0; bottom: 0; width: 700px; height: 230px; }
  .brand-art {
    position: absolute; right: 70px; top: 140px; width: 150px; height: 100px;
    background: radial-gradient(ellipse at 50% 60%, var(--sky) 0%, rgba(185,201,227,.7) 45%, rgba(255,255,255,0) 72%);
  }
  .person { position: absolute; left: 48px; top: 88px; }
  .person::before {
    content: ""; position: absolute; left: -48px; top: 8px; width: 10px; height: 50px;
    background: var(--navy);
  }
  .person__name {
    font-family: "Mulish", "Century Gothic", sans-serif; font-weight: 800;
    font-size: 33px; color: var(--navy); line-height: 1.1;
  }
  .person__role { font-size: 20px; color: var(--ink-grey); margin-top: 2px; }
  .details {
    position: absolute; left: 48px; top: 190px; list-style: none;
    font-size: 17px; color: var(--ink-grey); line-height: 1.6;
  }
  .details li { display: flex; align-items: center; gap: 10px; }
  .details .icon { width: 16px; height: 16px; flex: none; }
  .details .spacer { height: 6px; }
</style>
</head>
<body>
<main class="sheet">
  <section class="card card--questions" aria-label="Card side with coaching questions">
    <div class="emblem-art" role="img" aria-label="Faint brand illustration of a figure leaping from a summit"></div>
    <ul class="questions">
      <li>What is the decision you have been avoiding?</li>
      <li>If you were at your best, what would you do right now?</li>
      <li>What's one action you could take in the next 10 minutes?</li>
    </ul>
  </section>

  <section class="card card--contact" aria-label="Card side with contact details">
    <div class="brand">
      <div class="brand__name">The Steady Forge</div>
      <div class="brand__tagline">Shape your next chapter</div>
    </div>

    <svg class="summit-band" viewBox="0 0 700 230" aria-hidden="true">
      <path fill="#213668" d="M0 200 L520 200 C545 195 550 150 565 125 C580 100 600 95 615 90 C635 83 645 60 665 55 L700 45 L700 230 L0 230 Z"/>
    </svg>
    <div class="brand-art" role="img" aria-label="Brand illustration of a figure leaping from a summit"></div>

    <div class="person">
      <div class="person__name">Ted Harlow</div>
      <div class="person__role">Manager</div>
    </div>

    <ul class="details">
      <li>CPC, CLC, MTT, ANLP</li>
      <li>Box 4619, Millbrook, NE 68901-4619</li>
      <li class="spacer"></li>
      <li>
        <svg class="icon" viewBox="0 0 16 16" aria-hidden="true"><path fill="#213668" d="M3.5 1.5l2.5 0 1 3.5-1.6 1.2a9 9 0 0 0 4.4 4.4L11 9l3.5 1v2.5c0 1-1 2-2 2A11 11 0 0 1 1.5 3.5c0-1 1-2 2-2z"/></svg>
        303-555-0147
      </li>
      <li>
        <svg class="icon" viewBox="0 0 16 16" aria-hidden="true"><rect x="1" y="3" width="14" height="10" rx="1" fill="#213668"/><path d="M1.5 3.8L8 9l6.5-5.2" fill="none" stroke="#fff" stroke-width="1.3"/></svg>
        harlow.ted@thesteadyforge.example
      </li>
      <li>
        <svg class="icon" viewBox="0 0 16 16" aria-hidden="true"><circle cx="8" cy="8" r="7" fill="#213668"/><path d="M1 8h14M8 1c-3 3.5-3 10.5 0 14M8 1c3 3.5 3 10.5 0 14" fill="none" stroke="#fff" stroke-width="1"/></svg>
        www.thesteadyforge.example
      </li>
    </ul>
  </section>
</main>
</body>
</html>
```